Themed design for packaging sleeve and box

1) Gable box 330w x 200d x 160h (image attached for illustration purposes)
2) Sleeve to wrap around our food trays - see image attached

See the images uploaded!!!
This should not be copied, as some are from our competitors and are subject to Copywrite but gives an idea what kind of packaging we would be creating

From all the designs submitted, we will choose one final design and work with this designer to create our full packaging range.....

Target Market(s)

Working adults and health mined people

Font styles to use
Sans Serif

Colors

Designer to choose colors to be used in the design.

Requirements
Must have
• A clean modern look, striking design
Same design in different colours (see the drink bottles idea)
1) meat in shades of red
2) fish in shades of blue
3) vegetable in shades of green
Nice to have
• abstract white against strong colours
use shapes or mosaic or shades of the same colours
Should not have
• overpacked designs with too much information

```html
<!DOCTYPE html>
<html lang="en">
<head>
<meta charset="utf-8">
<title>Verdella Sleeve Dieline – Thai Green Chicken Curry</title>
<link rel="stylesheet" href="https://fonts.googleapis.com/css2?family=Arimo&family=Bebas+Neue&family=EB+Garamond:wght@400;500&family=Jost:wght@400&display=swap">
<style>
  :root {
    --veg-green: #4cfd0b;
    --ink: #111111;
    --title-green: #4cf40e;
    --name-slate: #37423f;
    --body-grey: #4a4a4a;
    --paper: #ffffff;
  }
  * { margin: 0; padding: 0; box-sizing: border-box; }
  html, body { width: 1200px; height: 445px; overflow: hidden; background: var(--paper); }
  .canvas { position: relative; width: 1200px; height: 445px; font-family: "Arimo", Arial, sans-serif; color: var(--ink); }

  .measure { position: absolute; top: 8px; font-size: 24px; line-height: 1; transform: translateX(-50%); }

  .dieline { position: absolute; left: 8px; top: 48px; width: 1184px; height: 253px; border: 1px solid var(--ink); }
  .fold { position: absolute; top: 48px; width: 1px; height: 253px; background: var(--ink); }

  .flap-tab { position: absolute; left: 8px; top: 159px; width: 79px; height: 34px; background: var(--veg-green); }
  .front-panel { position: absolute; left: 215px; top: 47px; width: 400px; height: 254px; background: var(--veg-green); }

  .brand { position: absolute; font-family: "Jost", sans-serif; font-weight: 400; color: var(--paper); font-size: 27px; line-height: 1; white-space: nowrap; letter-spacing: 0.5px; }
  .brand--side { left: 321px; top: 172px; transform: translate(-50%, -50%) rotate(90deg); }
  .brand--top { left: 494px; top: 173px; transform: translate(-50%, -50%); }
  .brand--end { left: 913px; top: 175px; transform: translate(-50%, -50%) rotate(-90deg); color: var(--title-green); font-size: 29px; }

  .range-title { position: absolute; left: 639px; top: 158px; font-family: "EB Garamond", serif; font-weight: 500; font-size: 33px; color: var(--title-green); letter-spacing: 0.5px; line-height: 1; }
  .dish-name { position: absolute; left: 638px; top: 217px; font-family: "Bebas Neue", sans-serif; font-size: 24px; line-height: 25px; color: var(--name-slate); }
  .dish-desc { position: absolute; left: 639px; top: 270px; font-family: "EB Garamond", serif; font-size: 9.6px; line-height: 10.8px; color: var(--body-grey); }

  .end-copy { position: absolute; left: 964px; top: 174px; width: 200px; transform: translate(-50%, -50%) rotate(-90deg); font-family: "EB Garamond", serif; font-size: 8.4px; line-height: 10px; color: var(--body-grey); text-align: right; }

  .spec-notes { position: absolute; left: 502px; top: 325px; font-size: 24px; line-height: 28px; }
</style>
</head>
<body>
<main class="canvas">
  <span class="measure" style="left:105px">70</span>
  <span class="measure" style="left:291px">55</span>
  <span class="measure" style="left:607px">158</span>
  <span class="measure" style="left:925px">55</span>
  <span class="measure" style="left:1096px">60</span>

  <div class="dieline"></div>
  <div class="flap-tab"></div>
  <div class="front-panel"></div>
  <div class="fold" style="left:850px"></div>
  <div class="fold" style="left:1014px"></div>

  <span class="brand brand--side">verdella</span>
  <span class="brand brand--top">verdella</span>

  <h1 class="range-title">POTAGE</h1>
  <p class="dish-name">THAI GREEN<br>CHICKEN CURRY</p>
  <p class="dish-desc">Lorem ipsum dolor sit amet, consectetur<br>adipiscing elit. Morbi ultricies molestie orci.</p>

  <span class="brand brand--end">verdella</span>
  <p class="end-copy">Fusce placerat risus sit amet lectus egestas, pretium porttitor nisi facilisis. Morbi pellentesque odio et nulla interdum viverra. Nam suscipit, eros ut vulputate ultrices, libero odio</p>

  <p class="spec-notes">Top is 158<br>Bottom is 108 plus overlap<br>Sides 55<br>Width 85</p>
</main>
</body>
</html>
```